M&A Advisory firm needs elegant and powerful letterhead

We need a powerful but elegant letterhead to engage with the international financial industry.

Target Market(s)

New York and International Financial Industry

Industry/Entity Type

Finance

Font styles to use
Other font styles liked:
• Poppins

Requirements
Must have
• 482 W 71st Street 14th Floor New York, NY 10157 O: +1 (212) 555 0147 F: +1 (212) 555 0182

```html
<!DOCTYPE html>
<html lang="en">
<head>
<meta charset="utf-8">
<title>Halvern Letterhead</title>
<link rel="stylesheet" href="https://fonts.googleapis.com/css2?family=Poppins:wght@400&family=Roboto:wght@700&display=swap">
<style>
  :root {
    --brand-blue: #0f5495;
    --brand-grey: #808185;
    --tagline-grey: #6e6f73;
    --address-ink: #2f5b52;
    --paper: #ffffff;
    --backdrop: #e4e4e6;
  }
  * { margin: 0; padding: 0; box-sizing: border-box; }
  html, body {
    width: 1200px;
    height: 799px;
    overflow: hidden;
    background: var(--backdrop);
  }
  .letterhead {
    position: absolute;
    left: 338px;
    top: 30px;
    width: 523px;
    height: 739px;
    background: var(--paper);
    box-shadow: 0 2px 10px rgba(0, 0, 0, 0.12);
    overflow: hidden;
  }
  .band {
    position: absolute;
    left: 0;
    width: 523px;
    display: block;
  }
  .band--top { top: 0; }
  .band--bottom { bottom: 0; }
  .brand {
    position: absolute;
    left: 26px;
    top: 60px;
    display: flex;
    align-items: center;
    gap: 14px;
  }
  .brand__dot {
    width: 28px;
    height: 28px;
    border-radius: 50%;
    background: var(--brand-blue);
  }
  .brand__text { display: flex; flex-direction: column; }
  .brand__name {
    font-family: "Poppins", sans-serif;
    font-weight: 400;
    font-size: 35px;
    line-height: 1;
    color: var(--brand-blue);
    letter-spacing: 0.5px;
  }
  .brand__tagline {
    font-family: "Poppins", sans-serif;
    font-weight: 400;
    font-size: 7px;
    letter-spacing: 2.2px;
    color: var(--tagline-grey);
    margin-top: 3px;
  }
  .contact-line {
    position: absolute;
    left: 0;
    width: 523px;
    top: 677px;
    text-align: center;
    font-family: "Roboto", sans-serif;
    font-weight: 700;
    font-size: 9.4px;
    color: var(--address-ink);
    white-space: nowrap;
  }
</style>
</head>
<body>
  <main class="letterhead">
    <svg class="band band--top" width="523" height="42" viewBox="0 0 523 42" aria-hidden="true">
      <rect x="0" y="0" width="523" height="19.5" fill="var(--brand-blue)"/>
      <polygon points="0,19.5 523,19.5 523,26.9 218.5,26.9 200,41.8 0,41.8" fill="var(--brand-grey)"/>
    </svg>

    <header class="brand">
      <span class="brand__dot"></span>
      <div class="brand__text">
        <span class="brand__name">HALVERN</span>
        <span class="brand__tagline">Advisory Partners</span>
      </div>
    </header>

    <p class="contact-line">482 W 71st Street 14th Floor New York, NY 10157 O: +1 (212) 555 0147 F: +1 (212) 555 0182</p>

    <svg class="band band--bottom" width="523" height="32" viewBox="0 0 523 32" aria-hidden="true">
      <polygon points="346,0 523,0 523,21.5 0,21.5 0,14.5 328,14.5" fill="var(--brand-grey)"/>
      <rect x="0" y="21.5" width="523" height="10.5" fill="var(--brand-blue)"/>
    </svg>
  </main>
</body>
</html>
```